Brackwell HVAC Service LLC Business Card

We just got a design created by one of your designers for a logo and now would like help with a business card design. The information to be included on the card is as follows:
Brackwell HVAC Service LLC (I will attach logo design)
P.O. Box 418
Marlow Creek, NE 69990
(555) 555-0147
Dale Vonnholt
I might include an e-mail address, but I'm not sure yet.
Target Market(s)
Customers needing service or repairs done on their heating and air conditioning systems.
Industry/Entity Type
Business
Contact Information for Business Card
P.O. Box 418
Marlow Creek, NE 69990
(555) 555-0147
Dale Vonnholt

```html
<!DOCTYPE html>
<html lang="en">
<head>
<meta charset="utf-8">
<title>Brackwell HVAC Service LLC – Business Card</title>
<link rel="stylesheet" href="https://fonts.googleapis.com/css2?family=Roboto+Condensed:wght@400;700&display=swap">
<style>
  :root {
    --brand-red: #e8202e;
    --brand-blue: #1b56a4;
    --card-white: #ffffff;
    --backdrop: #ecebe8;
  }
  * { margin: 0; padding: 0; box-sizing: border-box; }
  html, body {
    width: 1200px;
    height: 1000px;
    overflow: hidden;
    background: var(--backdrop);
    font-family: "Roboto Condensed", "Arial Narrow", sans-serif;
  }
  .business-card {
    position: absolute;
    left: 162px;
    top: 250px;
    width: 875px;
    height: 500px;
    background: var(--card-white);
    overflow: hidden;
    box-shadow: 0 10px 30px rgba(0,0,0,0.18);
  }
  .card-shapes {
    position: absolute;
    inset: 0;
    width: 875px;
    height: 500px;
  }
  .brand-lockup {
    position: absolute;
    left: 60px;
    top: 95px;
    display: flex;
    align-items: center;
    gap: 18px;
    color: var(--card-white);
  }
  .brand-dot {
    width: 74px;
    height: 74px;
    border-radius: 50%;
    background: var(--card-white);
    flex: none;
  }
  .brand-name {
    font-weight: 700;
    font-size: 38px;
    line-height: 1.0;
    letter-spacing: 0.5px;
    text-transform: uppercase;
  }
  .contact-block {
    position: absolute;
    right: 40px;
    top: 205px;
    text-align: right;
    color: var(--brand-blue);
  }
  .contact-name {
    font-weight: 700;
    font-size: 40px;
    line-height: 1.1;
    margin-bottom: 8px;
  }
  .contact-line {
    font-weight: 400;
    font-size: 32px;
    line-height: 1.2;
  }
</style>
</head>
<body>
  <div class="business-card">
    <svg class="card-shapes" viewBox="0 0 875 500" aria-hidden="true">
      <path d="M0,0 H840 C790,110 600,170 420,225 C230,285 80,360 35,478 H0 Z" fill="var(--brand-red)"/>
      <rect x="0" y="478" width="875" height="5" fill="var(--brand-red)"/>
      <rect x="0" y="483" width="875" height="17" fill="var(--brand-blue)"/>
    </svg>

    <div class="brand-lockup">
      <div class="brand-dot"></div>
      <div class="brand-name">Brackwell HVAC<br>Service LLC</div>
    </div>

    <div class="contact-block">
      <p class="contact-name">Dale Vonnholt</p>
      <p class="contact-line">P.O. Box 418</p>
      <p class="contact-line">Marlow Creek, NE 69990</p>
      <p class="contact-line">(555) 555-0147</p>
    </div>
  </div>
</body>
</html>
```